Pebble Wren Childcare centre needs a new LED outdoor banner

We need a new outdoor banner for our pre-school. It needs to be around 2440 mm x 1220 mm. It will be lit at night so I need it to stand out. I'm looking for a modern upbeat design. It will have my logo in the middle which is a graduation teddy bear with our name and phone number on it. I'm happy to experiment with different design options as mine is 20 years old. It needs to be colorful, inviting and very "in your face" and child friendly. It will be located near the fence of the property so it will be seen by cars driving by at a speed of around 50KM/H. So it needs to be clear, big bold fonts and bright colors. Thank you!

```html
<!DOCTYPE html>
<html lang="en">
<head>
<meta charset="utf-8">
<title>Pebble Wren Childcare Centre – Outdoor Banner</title>
<link rel="stylesheet" href="https://fonts.googleapis.com/css2?family=Fira+Sans:wght@600;800&display=swap">
<style>
  :root {
    --pink: #ff0090;
    --yellow: #fff200;
    --cyan: #00d8ff;
    --green: #22dc12;
    --white: #ffffff;
    --name: #ffffff;
  }
  html, body {
    margin: 0;
    padding: 0;
    overflow: hidden;
    background: var(--pink);
  }
  .banner {
    position: relative;
    width: 1200px;
    height: 600px;
    overflow: hidden;
    background: var(--pink);
    font-family: "Fira Sans", Arial, sans-serif;
  }
  .rays {
    position: absolute;
    inset: 0;
    width: 1200px;
    height: 600px;
  }
  .ray-yellow { fill: var(--yellow); }
  .ray-cyan { fill: var(--cyan); }
  .ray-green { fill: var(--green); }

  .brand {
    position: absolute;
    left: 0;
    top: 150px;
    width: 1200px;
    text-align: center;
    color: var(--name);
    font-weight: 800;
    line-height: 1;
  }
  .brand-name {
    display: block;
    font-size: 132px;
    letter-spacing: 1px;
  }
  .brand-sub {
    display: block;
    margin-top: 18px;
    font-size: 74px;
  }

  .info {
    position: absolute;
    color: var(--yellow);
    font-weight: 600;
    font-size: 36px;
    line-height: 48px;
    text-transform: uppercase;
    letter-spacing: 0.5px;
    margin: 0;
  }
  .info-ages { left: 203px; top: 452px; }
  .info-hours { left: 203px; top: 500px; }
  .info-phone { left: 564px; top: 452px; }
  .info-address { left: 868px; top: 452px; line-height: 37px; }

  .icon {
    position: absolute;
    fill: none;
    stroke: var(--white);
    stroke-width: 4;
    stroke-linecap: round;
    stroke-linejoin: round;
  }
  .icon-kids {
    position: absolute;
    left: 88px;
    top: 436px;
    width: 100px;
    height: 56px;
    border-radius: 28px;
    background: linear-gradient(90deg, #ffffff 0%, #ffd6ec 100%);
  }
  .icon-clock { left: 146px; top: 500px; width: 44px; height: 44px; }
  .icon-phone { left: 505px; top: 472px; width: 46px; height: 46px; }
  .icon-pin { left: 816px; top: 456px; width: 36px; height: 46px; }
  .icon-pin .pin-body { fill: var(--white); stroke: none; }
  .icon-pin .pin-hole { fill: var(--pink); stroke: none; }
</style>
</head>
<body>
<main class="banner">
  <svg class="rays" viewBox="0 0 1200 600" aria-hidden="true">
    <polygon class="ray-yellow" points="0,0 560,80 640,80 1200,5 1200,100 640,165 560,165 0,133"/>
    <polygon class="ray-cyan" points="0,133 560,165 640,165 1200,100 1200,313 640,310 560,310 0,338"/>
    <polygon class="ray-green" points="0,338 560,310 640,310 1200,313 1200,432 640,405 560,405 0,433"/>
  </svg>

  <h1 class="brand">
    <span class="brand-name">Pebble Wren</span>
    <span class="brand-sub">Childcare Centre</span>
  </h1>

  <div class="icon-kids" role="img" aria-label="Small icon of two children"></div>
  <p class="info info-ages">0 - 6 Years</p>

  <svg class="icon icon-clock" viewBox="0 0 44 44" aria-hidden="true">
    <circle cx="22" cy="22" r="19"/>
    <polyline points="22,11 22,23 31,23"/>
  </svg>
  <p class="info info-hours">7.30am - 5.30pm</p>

  <svg class="icon icon-phone" viewBox="0 0 46 46" aria-hidden="true">
    <path d="M10 4 L17 4 L20 14 L15 18 C18 25 22 29 28 32 L32 27 L42 30 L42 37 C42 40 40 42 37 42 C19 41 5 27 4 9 C4 6 6 4 10 4 Z"/>
  </svg>
  <p class="info info-phone">02 5550 1482<br>0400 555 217</p>

  <svg class="icon icon-pin" viewBox="0 0 36 46" aria-hidden="true">
    <path class="pin-body" d="M18 0 C8 0 0 8 0 17 C0 29 18 46 18 46 C18 46 36 29 36 17 C36 8 28 0 18 0 Z"/>
    <circle class="pin-hole" cx="18" cy="17" r="7"/>
  </svg>
  <p class="info info-address">48 Orchard St,<br>Maple Grove<br>NSW 2999</p>
</main>
</body>
</html>
```